Personal Training Business Card Design

I have just started my own personal training business called "Lana Corvell Fitness". My goal as a personal trainer is to motivate, inspire and educate all of my clients about the benefits of regular exercise, nourishing the body with nutritious foods and living healthy. I train both men and women, so I would like a business card that will appeal to both sexes and not come across too feminine or too masculine. I'm looking for a fresh, yet simple look which uses "fresh" colours such as green, white and grey - similar to my logo (but open to other effective gender-neutral colour schemes). I am open to using the logo I have uploaded as one image together, or separating the text and image (also supplied).
Industry/Entity Type
Personal Trainer
Contact Information for Business Card
Lana Corvell
Fitness Coach
Address: Ground Floor, Maplewick House, 342 Larkin St, Harlow Bay, 5120
Email: lanacorvellfitness@mailorbit.net
Phone: 0455 293 604
Facebook: www.socialnook.net/lanacorvellfitness
Look and feel

```html
<!DOCTYPE html>
<html lang="en">
<head>
<meta charset="utf-8">
<title>Lana Corvell Fitness – Business Cards</title>
<link href="https://fonts.googleapis.com/css2?family=Quicksand:wght@400;500;600&display=swap" rel="stylesheet">
<style>
  :root {
    --green: #7dc142;
    --grey: #77787b;
    --text-grey: #6d6e71;
    --card: #ffffff;
    --backdrop: #e9e9e9;
  }
  * { margin: 0; padding: 0; box-sizing: border-box; }
  html, body { width: 1200px; height: 900px; overflow: hidden; }
  body {
    background: var(--backdrop);
    font-family: "Quicksand", sans-serif;
    position: relative;
  }
  .card {
    position: absolute;
    width: 540px;
    height: 310px;
    background: var(--card);
    box-shadow: 0 6px 18px rgba(0,0,0,0.12);
    overflow: hidden;
  }
  .card-front { left: 600px; top: 110px; }
  .card-back { left: 70px; top: 470px; }
  .stripes { position: absolute; left: 0; top: 0; width: 540px; height: 310px; }

  /* front */
  .brand-block {
    position: absolute; left: 25px; top: 68px; width: 240px; text-align: center;
  }
  .brand-mark {
    width: 70px; height: 70px; border-radius: 50%;
    background: var(--green); margin: 0 auto 10px;
  }
  .brand-name {
    font-weight: 600; font-size: 17px; color: var(--green);
    letter-spacing: 0.5px; text-transform: uppercase; white-space: nowrap;
  }
  .brand-tagline {
    font-size: 13px; color: var(--grey); margin-top: 2px;
  }
  .contact {
    position: absolute; left: 285px; top: 36px; width: 250px;
  }
  .contact-group {
    border-left: 2px solid var(--green);
    padding-left: 12px; margin-bottom: 14px;
  }
  .contact-name { font-size: 21px; color: var(--green); font-weight: 500; line-height: 1.15; }
  .contact-role { font-size: 12px; color: var(--text-grey); }
  .contact-line { font-size: 11.5px; color: var(--text-grey); line-height: 1.45; white-space: nowrap; }
  .label { color: var(--green); }
  .web-handle { color: var(--green); }

  /* back */
  .back-brand {
    position: absolute; left: 0; top: 72px; width: 540px;
    display: flex; align-items: center; justify-content: center; gap: 14px;
  }
  .back-brand .brand-mark { width: 56px; height: 56px; margin: 0; }
  .back-brand .brand-name { font-size: 26px; }
  .back-tagline {
    position: absolute; left: 0; bottom: 20px; width: 540px; text-align: center;
    font-size: 14px; letter-spacing: 7px; color: var(--green);
  }
</style>
</head>
<body>

  <section class="card card-front">
    <svg class="stripes" viewBox="0 0 540 310" aria-hidden="true">
      <polygon points="0,212 244,212 240,220 0,220" fill="var(--green)"/>
      <polygon points="256,240 392,240 386,250 250,250" fill="var(--grey)"/>
      <polygon points="404,274 540,274 540,284 400,284" fill="var(--green)"/>
    </svg>
    <div class="brand-block">
      <div class="brand-mark"></div>
      <div class="brand-name">Lana Corvell Fitness</div>
      <div class="brand-tagline">energise. empower. evolve.</div>
    </div>
    <div class="contact">
      <div class="contact-group">
        <div class="contact-name">Lana Corvell</div>
        <div class="contact-role">Fitness Coach</div>
      </div>
      <div class="contact-group">
        <div class="contact-line">Ground Floor, Maplewick House,</div>
        <div class="contact-line">342 Larkin St, Harlow Bay, 5120</div>
      </div>
      <div class="contact-group">
        <div class="contact-line"><span class="label">P:</span> 0455 293 604</div>
        <div class="contact-line"><span class="label">E:</span> lanacorvellfitness@mailorbit.net</div>
        <div class="contact-line">www.socialnook.net/<span class="web-handle">lanacorvellfitness</span></div>
      </div>
    </div>
  </section>

  <section class="card card-back">
    <svg class="stripes" viewBox="0 0 540 310" aria-hidden="true">
      <polygon points="0,238 200,238 196,246 0,246" fill="var(--green)"/>
      <polygon points="206,222 330,222 324,232 200,232" fill="var(--grey)"/>
      <polygon points="336,206 540,206 540,214 332,214" fill="var(--green)"/>
    </svg>
    <div class="back-brand">
      <div class="brand-mark"></div>
      <div class="brand-name">Lana Corvell Fitness</div>
    </div>
    <div class="back-tagline">energise. empower. evolve.</div>
  </section>

</body>
</html>
```